Full Page print dental ad

Looking for a modern dental ad to promote our office and an Tovamerk special $500 off and also show our Dumek techology.

website is marlowbrookdental.com
address is 24417 53rd ave NE Alderwick, WA 98771
Phone is 360-555-0193

attached an ad that this will be replaceing, but we do not like it. but it has information that might be helpful.

looks for something a more modern and less busy

```html
<!DOCTYPE html>
<html lang="en">
<head>
<meta charset="utf-8">
<title>Marlow Brook – Your Local Family Dentist</title>
<link href="https://fonts.googleapis.com/css2?family=Lato:wght@400;700;900&family=Oswald:wght@400;500;600&display=swap" rel="stylesheet">
<style>
  :root {
    --green: #5cb152;
    --green-dark: #3f7d38;
    --green-deep: #2f6a2b;
    --black: #141414;
    --ink: #1d1d1d;
    --grey-panel: #e4e5e7;
    --grey-box: #dcdee1;
    --white: #ffffff;
    --blue: #2a9fd8;
  }
  * { box-sizing: border-box; margin: 0; padding: 0; }
  html, body { width: 854px; height: 1200px; overflow: hidden; background: #f4f4f4; }
  body { font-family: "Lato", sans-serif; color: var(--ink); }
  .ad { position: relative; width: 854px; height: 1200px; overflow: hidden;
        background: linear-gradient(180deg, #ffffff 48%, #eceeef 100%); }

  /* Hero */
  .hero-panel { position: absolute; left: 0; top: 0; width: 393px; height: 353px; background: var(--grey-panel); }
  .headline { position: absolute; left: 32px; top: 18px; font-weight: 900;
              font-size: 70px; line-height: 71px; letter-spacing: -1px; }
  .headline .dark { color: var(--black); display: block; }
  .headline .accent { color: var(--green); display: block; }
  .hero-photo { position: absolute; left: 393px; top: 0; width: 461px; height: 353px;
                background: linear-gradient(120deg, #dfe6ea 0%, #c9d6dc 40%, #eef1f2 70%, #d8dcd8 100%); }
  .patients-band { position: absolute; left: 0; top: 312px; width: 393px; height: 41px; background: var(--green-dark);
                   color: var(--white); font-family: "Oswald", sans-serif; font-weight: 500; font-size: 23px;
                   line-height: 41px; padding-left: 35px; letter-spacing: 0.3px; }

  /* Features */
  .features { position: absolute; left: 0; top: 353px; width: 854px; height: 222px; background: var(--black); }
  .feature-list { position: absolute; top: 42px; list-style: none; }
  .feature-list.left { left: 34px; }
  .feature-list.right { left: 469px; }
  .feature-list li { color: #e8e8e8; font-size: 15px; line-height: 19px; height: 38.5px; display: flex; align-items: flex-start; }
  .feature-list svg { width: 15px; height: 15px; margin: 2px 14px 0 0; flex: none; }

  .safety-note { position: absolute; left: 36px; top: 570px; width: 784px; height: 84px; background: var(--green);
                 border-radius: 5px; color: var(--white); font-size: 18.5px; line-height: 26px; padding: 17px 40px 17px 16px; }

  /* Credentials */
  .credentials { position: absolute; left: 36px; top: 676px; width: 352px; height: 299px; background: var(--grey-box);
                 border-radius: 4px; box-shadow: 0 1px 4px rgba(0,0,0,0.12); text-align: center; }
  .award-badge { position: absolute; left: 54px; top: 23px; width: 241px; height: 67px; border: 1.5px solid #555;
                 background: #eceef0; }
  .award-years { position: absolute; top: 100px; width: 100%; font-size: 13.5px; color: #333; }
  .provider-label { position: absolute; top: 158px; width: 100%; font-size: 26px; color: var(--black); }
  .provider-label em { font-style: normal; color: var(--green-dark); }
  .provider-name { position: absolute; top: 204px; left: 0; width: 100%; display: flex; justify-content: center; align-items: center; gap: 12px; }
  .provider-name .dot { width: 34px; height: 34px; border-radius: 50%; background: var(--blue); }
  .provider-name .word { font-size: 38px; color: var(--blue); font-weight: 400; }
  .provider-tag { position: absolute; top: 253px; left: 0; width: 100%; font-size: 14px; letter-spacing: 5px; color: #666; }

  .office-photo { position: absolute; top: 677px; width: 190px; height: 131px; }
  .office-photo.exterior { left: 420px; background: linear-gradient(180deg, #c9d3dc 0%, #8a99a8 55%, #b8a35a 100%); }
  .office-photo.interior { left: 628px; background: linear-gradient(135deg, #8b7c6c 0%, #b9b3a8 45%, #6f8e4a 75%, #8a6a4a 100%); }

  /* Special */
  .special-tab { position: absolute; left: 481px; top: 828px; width: 296px; height: 34px; background: var(--green);
                 color: var(--white); font-weight: 700; font-size: 22px; text-align: center;
                 line-height: 34px; letter-spacing: 0.5px; z-index: 2; }
  .special-box { position: absolute; left: 420px; top: 850px; width: 400px; height: 125px; background: var(--black); }
  .special-price { position: absolute; left: 20px; top: 26px; font-family: "Oswald", sans-serif; font-weight: 600;
                   font-size: 62px; line-height: 62px; color: var(--green); }
  .special-caption { position: absolute; left: 28px; top: 95px; font-size: 12px; color: var(--white); text-decoration: underline;
                     letter-spacing: 0.5px; font-weight: 700; }
  .special-divider { position: absolute; left: 164px; top: 30px; width: 1px; height: 72px; background: #666; }
  .tech-name { position: absolute; left: 182px; top: 24px; font-family: "Oswald", sans-serif; font-size: 50px; line-height: 56px; color: #6a6c6e; }
  .tech-tag { position: absolute; left: 182px; top: 93px; font-size: 17px; letter-spacing: 2px; color: #9a9c9e; font-weight: 700; }

  /* Coupon */
  .coupon { position: absolute; left: 36px; top: 996px; width: 781px; height: 87px; border: 1.5px solid var(--green); border-radius: 4px; background: var(--white); }
  .coupon-free { position: absolute; left: 14px; top: 8px; font-family: "Oswald", sans-serif; font-weight: 600; font-size: 62px;
                 line-height: 68px; color: var(--green-deep); letter-spacing: 3px; }
  .coupon-divider { position: absolute; left: 172px; top: 14px; width: 1px; height: 58px; background: #999; }
  .coupon-title { position: absolute; left: 184px; top: 14px; font-size: 14.5px; letter-spacing: 0.2px; color: var(--ink); }
  .coupon-terms { position: absolute; left: 184px; top: 35px; font-size: 9.5px; line-height: 12px; font-weight: 700; color: var(--ink); }
  .coupon-expiry { position: absolute; left: 184px; top: 64px; font-size: 9.5px; letter-spacing: 2px; color: var(--green-dark); }

  /* Footer */
  .footer { position: absolute; left: 0; top: 1098px; width: 854px; height: 102px; background: #e6e7e8; border-top: 2px solid var(--black); }
  .contact-tab { position: absolute; left: 324px; top: 0; width: 124px; height: 20px; background: var(--green-dark); color: var(--white);
                 font-family: "Oswald", sans-serif; font-size: 14px; line-height: 20px; text-align: center; letter-spacing: 0.3px; }
  .brand { position: absolute; left: 36px; top: 28px; display: flex; align-items: center; gap: 10px; }
  .brand .mark { width: 50px; height: 50px; border-radius: 50%; border: 3px solid var(--black); }
  .brand-name { font-size: 19px; color: var(--black); }
  .brand-tag { font-size: 10px; color: #444; margin-left: 20px; }
  .contact-col { position: absolute; top: 48px; border-left: 1.5px solid #333; padding-left: 14px; height: 36px; }
  .contact-col.left { left: 340px; }
  .contact-col.right { left: 648px; }
  .contact-col p { font-size: 10.5px; line-height: 17px; color: var(--black); display: flex; align-items: center; gap: 8px; }
  .contact-col svg { width: 9px; height: 9px; flex: none; }
</style>
</head>
<body>
<main class="ad">
  <section class="hero">
    <div class="hero-panel">
      <h1 class="headline"><span class="dark">YOUR</span><span class="dark">LOCAL</span><span class="accent">FAMILY</span><span class="accent">DENTIST</span></h1>
    </div>
    <div class="hero-photo" role="img" aria-label="Smiling dental assistant in a white coat with a dentist working in a bright treatment room behind her"></div>
    <div class="patients-band">NOW ACCEPTING NEW PATIENTS</div>
  </section>

  <section class="features">
    <ul class="feature-list left">
      <li><svg viewBox="0 0 15 15"><rect x="1" y="1" width="13" height="13" fill="none" stroke="#ffffff" stroke-width="1.3"/><path d="M3.5 7.5l3 3 5.5-6" fill="none" stroke="#5cb152" stroke-width="2"/></svg>Family Owned &amp; Operated Dental Office</li>
      <li><svg viewBox="0 0 15 15"><rect x="1" y="1" width="13" height="13" fill="none" stroke="#ffffff" stroke-width="1.3"/><path d="M3.5 7.5l3 3 5.5-6" fill="none" stroke="#5cb152" stroke-width="2"/></svg>Most Dental insurances Accepted</li>
      <li><svg viewBox="0 0 15 15"><rect x="1" y="1" width="13" height="13" fill="none" stroke="#ffffff" stroke-width="1.3"/><path d="M3.5 7.5l3 3 5.5-6" fill="none" stroke="#5cb152" stroke-width="2"/></svg>Medical Grade HEPA Filters throughout office</li>
      <li><svg viewBox="0 0 15 15"><rect x="1" y="1" width="13" height="13" fill="none" stroke="#ffffff" stroke-width="1.3"/><path d="M3.5 7.5l3 3 5.5-6" fill="none" stroke="#5cb152" stroke-width="2"/></svg>All COVID Safety Precautions Implemented</li>
    </ul>
    <ul class="feature-list right">
      <li><svg viewBox="0 0 15 15"><rect x="1" y="1" width="13" height="13" fill="none" stroke="#ffffff" stroke-width="1.3"/><path d="M3.5 7.5l3 3 5.5-6" fill="none" stroke="#5cb152" stroke-width="2"/></svg>Tovamerk Clear Aligners</li>
      <li><svg viewBox="0 0 15 15"><rect x="1" y="1" width="13" height="13" fill="none" stroke="#ffffff" stroke-width="1.3"/><path d="M3.5 7.5l3 3 5.5-6" fill="none" stroke="#5cb152" stroke-width="2"/></svg>Leading Edge Dental Technology</li>
      <li><svg viewBox="0 0 15 15"><rect x="1" y="1" width="13" height="13" fill="none" stroke="#ffffff" stroke-width="1.3"/><path d="M3.5 7.5l3 3 5.5-6" fill="none" stroke="#5cb152" stroke-width="2"/></svg>Early Mornings &amp; Evenings available</li>
      <li><svg viewBox="0 0 15 15"><rect x="1" y="1" width="13" height="13" fill="none" stroke="#ffffff" stroke-width="1.3"/><path d="M3.5 7.5l3 3 5.5-6" fill="none" stroke="#5cb152" stroke-width="2"/></svg><span>Over 250 5-Star Starlist Reviews...<br>FIND OUT WHY!</span></li>
    </ul>
  </section>

  <p class="safety-note">To ensure your safety we are following the guidelines &amp; recommendations put<br>into place by CDC, ADA, &amp; WISHA. Patient safety is our number one priority.</p>

  <section class="credentials">
    <div class="award-badge" role="img" aria-label="Top dentist award badge"></div>
    <p class="award-years">2016 | 2017 | 2018 | 2019 | 2020 | 2021</p>
    <p class="provider-label">Preferred <em>Provider</em> For:</p>
    <div class="provider-name"><span class="dot"></span><span class="word">Tovamerk</span></div>
    <p class="provider-tag">PROVIDER</p>
  </section>

  <div class="office-photo exterior" role="img" aria-label="Exterior of the dental office building with its entrance"></div>
  <div class="office-photo interior" role="img" aria-label="Modern waiting room interior of the dental office"></div>

  <section class="special">
    <div class="special-tab">TOVAMERK SPECIAL</div>
    <div class="special-box">
      <p class="special-price">$500</p>
      <p class="special-caption">SPECIAL OFFER</p>
      <div class="special-divider"></div>
      <p class="tech-name">Dumek</p>
      <p class="tech-tag">DIGITAL PRACTICE</p>
    </div>
  </section>

  <section class="coupon">
    <p class="coupon-free">FREE</p>
    <div class="coupon-divider"></div>
    <p class="coupon-title">TEETH WHITENING FOR NEW PATIENTS WITH NEW PATIENT EXAM &amp; CLEANING</p>
    <p class="coupon-terms">Must mention Lakeline coupon at time of booking. Not valid with any other offers or specials or with insurance coverage,<br>new cash clients only.</p>
    <p class="coupon-expiry">EXPIRES 2/28/22.</p>
  </section>

  <footer class="footer">
    <div class="contact-tab">CONTACT US NOW</div>
    <div class="brand">
      <span class="mark"></span>
      <div>
        <p class="brand-name">marlow brook</p>
        <p class="brand-tag">family and cosmetic dentistry</p>
      </div>
    </div>
    <div class="contact-col left">
      <p><svg viewBox="0 0 10 10"><path d="M2 1l2 2-1 1.5c.8 1.3 1.7 2.2 3 3L7.5 6l2 2-1.3 1.5C4.5 9 1 5.5.5 1.8z" fill="#5cb152"/></svg>24417 53rd ave NE Alderwick, WA 98771</p>
      <p><svg viewBox="0 0 10 10"><path d="M5 0a3.5 3.5 0 0 0-3.5 3.5C1.5 6 5 10 5 10s3.5-4 3.5-6.5A3.5 3.5 0 0 0 5 0zm0 5a1.5 1.5 0 1 1 0-3 1.5 1.5 0 0 1 0 3z" fill="#5cb152"/></svg>hello@marlowbrookdental.com</p>
    </div>
    <div class="contact-col right">
      <p><svg viewBox="0 0 10 10"><rect x="0.5" y="2" width="9" height="6" fill="#5cb152"/><path d="M0.5 2l4.5 3.5L9.5 2" fill="none" stroke="#ffffff" stroke-width="0.8"/></svg>360-555-0193</p>
      <p><svg viewBox="0 0 10 10"><circle cx="5" cy="5" r="4.3" fill="none" stroke="#5cb152" stroke-width="1.2"/><path d="M0.7 5h8.6M5 0.7c-2 2.4-2 6.2 0 8.6M5 0.7c2 2.4 2 6.2 0 8.6" fill="none" stroke="#5cb152" stroke-width="0.8"/></svg>marlowbrookdental.com</p>
    </div>
  </footer>
</main>
</body>
</html>
```